Amber Tides: Lantern Tales from Seven Winters by the Northern Sea and Other Small Wonders

Good day! I am excited to work again with you, amazing designers! This time I am looking for the cover design of my book.
Dimensions 6” x 9”
The book name is as my name project. I love simplicity, but yet that is impactful. I love colours, I don't have a specific colour in mind, but I like the mustard colour as the one in the logo of my company. I am open to ideas! I have attached some cover samples that I like so that it gives a better idea of what I have on mind.
I am looking for something that looks professional, yet, not super serious, that it's approachable to people. Something that calls their attention at first glance.
I am working with my editor and my interior designer as well to finalize this part of the book. I will be working with the person that I select for the book design to finalize it.
About the book, here a passage of an unedited version of the introduction for guidance :
My intention is to take you on a journey to help you to understand what is going on in your mind so that you get out from anything that is holding you back in your life. My intention is to guide you to start fully living and experiencing a life that your mind even have yet conceived. To experience a life where you live fearless and without suffering. Living your life where you are the navigator and the creator of how you are experiencing it and you are living in a world of possibilities where there are no limitations.
For it, we will start to understand more about the mind and about the brain. I am not a neuroscientist and neither I consider my self an expert in the workings of the brain, what I know is the result of my fascination about our brain. This curiosity and the part of me that likes to understand how things work took me to read, research and learn about how our brain works and how its intrinsic mechanisms are subconsciously influencing and limiting us. I encourage you to stay on this part, it can be a bit technical, but understanding how it works will empower you not to allow your mind to dictate the way you approach your life and to live on autopilot.
We will continue to describe how you have been programmed throughout your life, putting you inside a box limited by your subconscious beliefs and ideas about the world. In this part, we will also discuss what ego is, how it is subconsciously limiting you and how the ways of when ego manifests itself are limiting you and making you suffer. Now that you know how you have been enclosed in your mind for all your life, we will move to discuss how you can get out of it. You will learn how to master your emotions to eliminate your suffering and not allow them to control the direction of your life and use them as a mechanism to get out from your programed mind. We continue to discuss how to leverage the power of your mind and harness your power of choice. Finally, I invite you to see yourself as a holistic being so that you start truly living and take control over the direction of your life, by nourishing and taking care of all those aspects of you utilizing their wisdom and synergy to achieve higher connection within yourself, your soul and live your life in a higher level of consciousness with peace, flow, love and purpose.

```html
<!DOCTYPE html>
<html lang="en">
<head>
<meta charset="utf-8">
<title>Amber Tides – Book Cover</title>
<link rel="stylesheet" href="https://fonts.googleapis.com/css2?family=Barlow+Condensed:wght@700&family=Barlow:wght@500&display=swap">
<style>
  :root {
    --stage: #f1f1f1;
    --mustard: #fbb41a;
    --mustard-deep: #f2a516;
    --orange: #f7841a;
    --ink: #0b0b0b;
    --paper: #ffffff;
    --logo-text: #f3a712;
  }
  * { margin: 0; padding: 0; box-sizing: border-box; }
  html, body {
    width: 1200px; height: 1074px; overflow: hidden;
    background: var(--stage);
  }
  .cover {
    position: absolute;
    left: 274px; top: 47px;
    width: 652px; height: 980px;
    background: linear-gradient(180deg, var(--mustard) 0%, var(--mustard-deep) 100%);
    box-shadow: 0 18px 40px rgba(0,0,0,.18);
    overflow: hidden;
  }
  .band {
    position: absolute; left: 0; width: 100%;
    background: var(--orange);
  }
  .band--top { top: 90px; height: 78px; }
  .band--bottom { top: 800px; height: 86px; }
  .publisher {
    position: absolute;
    left: 352px; top: 112px;
    width: 272px; height: 150px;
    background: var(--paper);
    display: flex; align-items: center; justify-content: center; gap: 12px;
  }
  .publisher__dot {
    flex-shrink: 0;
    width: 26px; height: 26px; border-radius: 50%;
    background: var(--logo-text);
  }
  .publisher__name {
    font-family: "Barlow", sans-serif; font-weight: 500;
    font-size: 20px; letter-spacing: .02em; white-space: nowrap;
    color: var(--logo-text); text-transform: uppercase;
  }
  .title {
    position: absolute; left: 70px; top: 296px;
    font-family: "Barlow Condensed", sans-serif; font-weight: 700;
    font-size: 66px; line-height: .9; white-space: nowrap;
    color: var(--ink); text-transform: uppercase;
  }
  .subtitle {
    position: absolute; left: 72px; top: 690px;
    font-family: "Barlow", sans-serif; font-weight: 500;
    font-size: 27px; line-height: 1.1; white-space: nowrap;
    color: var(--ink);
  }
  .author {
    position: absolute; left: 72px; top: 818px;
    font-family: "Barlow", sans-serif; font-weight: 500;
    font-size: 28px; color: var(--paper);
  }
</style>
</head>
<body>
  <main class="cover">
    <div class="band band--top"></div>
    <div class="publisher">
      <span class="publisher__dot"></span>
      <span class="publisher__name">Brightfield Minds</span>
    </div>
    <h1 class="title">Amber Tides:<br>Lantern Tales From<br>Seven Winters By<br>The Northern Sea<br>And Other Small<br>Wonders</h1>
    <p class="subtitle">Experience A Life Where You<br>Live Fearless And Without Suffering</p>
    <div class="band band--bottom"></div>
    <p class="author">Author Name</p>
  </main>
</body>
</html>
```